Company: Plant Grillhouse
We make Plant Grillhouse more popular.
We are producing cooking books and spices.
For our spices (5 sorts) we need an label design.
Measurments of the label: 255mm x 55mm ( small changes of the exact measurements could follow in the next few days)
Name of the sorts:
- Sunny Zestpepper (Yellow)
- Desert Caravan (Orange/Brown)
- Charred Ember-Rub (Red)
- Charm of Tuscany (Green)
- Bold Shallotine (Black)
Attached you can find our main brand.
You can see we try to be clean and simple.
The package is a square glass with a cork closure
4 Side.
Side 1: Logo and Spice Name
Side 2: Incredients and Company Information
Side 3: Nice grphic that matches the sort of the spice
Side 4: Short story of the product and its added value
We look forward to cool suggestions.
Regards
Tobias
We want make the vegan lifestyle more cool.
So therefore don`t choose a too much ecological way, that is not up to date.

```html
<!DOCTYPE html>
<html lang="de">
<head>
<meta charset="utf-8">
<title>Bold Shallotine – Gewürzetikett</title>
<link href="https://fonts.googleapis.com/css2?family=Oswald:wght@500&family=Montserrat:wght@400;700&display=swap" rel="stylesheet">
<style>
  :root {
    --ink: #000000;
    --paper: #ffffff;
    --herb-grey: #2a2a2a;
    --herb-light: #4a4a4a;
  }
  * { margin: 0; padding: 0; box-sizing: border-box; }
  html, body { width: 1200px; height: 259px; overflow: hidden; background: var(--ink); }
  .label {
    position: relative;
    width: 1200px;
    height: 259px;
    background: var(--ink);
    color: var(--paper);
    font-family: "Montserrat", sans-serif;
  }
  .herb-art {
    position: absolute;
    left: 0; top: 0;
    width: 373px; height: 206px;
    background: radial-gradient(ellipse at 40% 50%, var(--herb-light) 0%, var(--herb-grey) 55%, var(--ink) 100%);
  }
  .herb-art--edge {
    left: 1173px; top: 36px;
    width: 27px; height: 114px;
    background: linear-gradient(90deg, var(--ink), var(--herb-grey));
  }
  .spice-name {
    position: absolute;
    left: 481px; top: 52px;
    transform: translateX(-50%);
    font-family: "Oswald", sans-serif;
    font-weight: 500;
    font-size: 49px;
    line-height: 57px;
    letter-spacing: 0.2em;
    text-align: center;
    text-transform: uppercase;
    white-space: nowrap;
  }
  .column-title {
    font-weight: 700;
    font-size: 10px;
    letter-spacing: 0.2em;
    text-transform: uppercase;
    text-align: center;
  }
  .story {
    position: absolute;
    left: 769px; top: 23px;
    transform: translateX(-50%);
    width: 260px;
    text-align: center;
  }
  .story__text {
    margin-top: 14px;
    font-size: 10.5px;
    line-height: 16px;
    letter-spacing: 0.13em;
  }
  .nutrition {
    position: absolute;
    left: 973px; top: 23px;
    width: 186px;
  }
  .nutrition .column-title { margin-left: 6px; }
  .nutrition__list { list-style: none; margin-top: 14px; font-size: 10.5px; line-height: 16px; letter-spacing: 0.1em; }
  .nutrition__row { display: flex; white-space: nowrap; }
  .nutrition__leader { flex: 1; overflow: hidden; }
  .company {
    margin-top: 13px;
    font-weight: 700;
    font-size: 10px;
    letter-spacing: 0.2em;
    text-align: center;
  }
  .divider {
    position: absolute;
    left: 0; top: 206px;
    width: 1200px; height: 3px;
    background: var(--paper);
  }
  .brand {
    position: absolute;
    left: 394px; top: 222px;
    display: flex; align-items: center; gap: 14px;
  }
  .brand__dot { width: 24px; height: 24px; border-radius: 50%; background: var(--paper); }
  .brand__name { font-weight: 700; font-size: 13.5px; letter-spacing: 0.02em; text-transform: uppercase; }
</style>
</head>
<body>
<main class="label">
  <div class="herb-art" role="img" aria-label="Line drawing of basil, chili peppers, garlic and rosemary in grey on black"></div>
  <div class="herb-art herb-art--edge" role="img" aria-label="Edge of a basil leaf drawing continuing around the jar"></div>

  <h1 class="spice-name">Bold<br>Shallotine</h1>

  <section class="story">
    <h2 class="column-title">Zestpepper-Gewürz:</h2>
    <p class="story__text">Geschichte des Gewürzes. Lorem ipsum dolor sit amet, consetetur sadipscing elitr, sed diam nonumy eirmod tempor invidunt ut labore et dolore magna aliquyam erat, sed diam voluptua.<br>sed diam nonumy eirmod tempor invidunt ut magna aliquyam erat, sed diam voluptua</p>
  </section>

  <section class="nutrition">
    <h2 class="column-title">Inhaltsstoffe:</h2>
    <ul class="nutrition__list">
      <li class="nutrition__row"><span>ENERGIE</span><span class="nutrition__leader">..............................</span><span>KJ/KCAL</span></li>
      <li class="nutrition__row"><span>FETT</span><span class="nutrition__leader">..............................................</span><span>G</span></li>
      <li class="nutrition__row"><span>KOHLENHYDRATE</span><span class="nutrition__leader">..............................</span><span>G</span></li>
      <li class="nutrition__row"><span>DAVON ZUCKER</span><span class="nutrition__leader">..............................</span><span>G</span></li>
      <li class="nutrition__row"><span>BALLASTSTOFFE</span><span class="nutrition__leader">..............................</span><span>G</span></li>
      <li class="nutrition__row"><span>EIWEISS</span><span class="nutrition__leader">..............................................</span><span>G</span></li>
      <li class="nutrition__row"><span>SALZ</span><span class="nutrition__leader">..............................................</span><span>G</span></li>
    </ul>
    <p class="company">PLANT GRILLHOUSE GMBH</p>
  </section>

  <div class="divider"></div>

  <div class="brand">
    <span class="brand__dot"></span>
    <span class="brand__name">Plant Grillhouse</span>
  </div>
</main>
</body>
</html>
```